Website Design for my Copper Distillation Equipment Business Nature Sciencey Theme

I already have a website www.halvorkettleworks.com and its a pixelhut website builder one. But I cannot get the design right at all. I need this fixed.

I have logo. I need a redesign, for my website, the home page, that maybe I can have something similar in design- I can use as template to copy, for other pages so the whole thing matches? Look at my website so you understand I have a few pages...but most are links. Its a competition. Code has to be easy for me to implement, I am not expert.

Your advice needed..It would be a plus if I can update this myself throughout time. If I could have this explained to me too, the maintenance of it...how would I do this too..etc..pretend I am a child when you explain, if you can. I am not good with this stuff but I am smart and can learn fast.

I want a high end look. Maybe like an ivy league college-y look too, real preppy, chemistry...science-y, nature like is good, leaves, drops water, fields of wheat, lavender, etc.

I want every page to look similar, but the home page is what I want to be the main showpiece,..and I want each page have a little text section, maybe a photos section and a video section, for that market. Like a nice website. If I am not doing this right, let me know. I can work with you. Just help me, please. Let me know if I am doing this right.

When I pick my winning design, for my website, I will hire the artist one-on-one to re-design my shopping cart next. Or if I need additional help with implementing this current design, I can hire the same artist again too. I have a blog that I may want to hire the redesign as well too, but later on. My point is I am not just looking for one project here but I want to follow up with winning artist. So it would be return business for the winner.

I got my logo done here so I am repeat customer. And I have given that winning artist other design work.

Target Market(s)

Moonshine Stills I sell most, Essential Oil Business, Micro and Craft Distilleries, Canna-businesses, Alcohol Fuel

Industry/Entity Type

Business

Number of Pages Required

5+ page

Colors
ec1f27

Requirements
Must have
• The categories for the stills must be prominent and eye catching. The main photo I would like to be naturelike theme, but you can try out different things with me. I am open to ideas and suggestions. I would like this to be implemented easy and fast.
Nice to have
• My logo in it. You can use any of my photos as well from my snapvale account. https://www.snapvale.net/photos/81726354@X07/
• Colors of my Logo...matching design.
• Maybe some basic stock photos you see would match for me..
• Chemistry like symbols for the categories, I love that.

```html
<!DOCTYPE html>
<html lang="en">
<head>
<meta charset="utf-8">
<title>Halvor Kettleworks – Copper Distillation Equipment</title>
<link href="https://fonts.googleapis.com/css2?family=Open+Sans:wght@400;600;700;800&display=swap" rel="stylesheet">
<style>
:root{
  --maroon:#5c1a20;
  --maroon-dark:#3f1014;
  --red:#7d1c23;
  --charcoal:#2b2b2b;
  --charcoal-dark:#1f1f1f;
  --ink:#333;
  --muted:#666;
  --light:#ececec;
  --white:#fff;
}
*{box-sizing:border-box;margin:0;padding:0}
html,body{width:1200px;height:2304px;overflow:hidden}
body{font-family:"Open Sans",Arial,sans-serif;color:var(--ink);background:var(--light);position:relative}
ul{list-style:none}
a{color:inherit;text-decoration:none}

/* top navigation */
.site-nav{position:absolute;top:0;left:0;width:1200px;height:80px;background:var(--maroon);z-index:3}
.site-nav ul{position:absolute;top:0;display:flex;height:80px;align-items:center;gap:38px;font-size:13px;font-weight:600;color:var(--white);letter-spacing:.5px}
.nav-left{left:88px}
.nav-right{right:88px}
.brand{position:absolute;left:540px;top:0;width:120px;height:122px;background:var(--white);border-radius:0 0 60px 60px;display:flex;flex-direction:column;align-items:center;justify-content:center;gap:6px;box-shadow:0 3px 8px rgba(0,0,0,.3)}
.brand-dot{width:14px;height:14px;border-radius:50%;background:var(--maroon)}
.brand-name{font-size:14px;font-weight:800;color:var(--maroon);text-align:center;line-height:1.15;text-transform:uppercase}

/* hero */
.hero{position:absolute;top:80px;left:0;width:1200px;height:460px;background:linear-gradient(120deg,#3c4a2c 0%,#6c7a48 30%,#a08560 55%,#5b4a3a 80%,#2d3324 100%)}
.hero-caption{position:absolute;left:88px;top:280px;width:520px;padding:16px 20px;background:rgba(20,20,20,.55);color:var(--white);font-size:28px;font-weight:700;line-height:1.3}
.hero-dots{position:absolute;left:88px;bottom:22px;display:flex;gap:8px}
.hero-dots span{width:10px;height:10px;border-radius:50%;background:rgba(255,255,255,.5)}
.hero-dots span:first-child{background:var(--white)}

/* intro */
.intro{position:absolute;top:540px;left:0;width:1200px;height:452px;background:var(--light)}
.category-box{position:absolute;left:88px;top:32px;width:224px;height:372px;background:var(--charcoal);color:#ddd;padding:18px 0}
.category-box h3{font-size:17px;color:var(--white);padding:0 20px 14px;font-weight:700;border-bottom:3px solid var(--red)}
.category-box li{font-size:13px;padding:8px 20px;border-bottom:1px solid #3d3d3d;display:flex;align-items:center;gap:10px}
.category-box li svg{flex:none}
.intro-copy{position:absolute;left:352px;top:32px;width:760px}
.intro-copy h2{font-size:26px;font-weight:600;color:var(--maroon);margin-bottom:10px}
.intro-copy p{font-size:13px;line-height:1.7;color:var(--muted)}
.how{position:absolute;left:352px;top:220px;width:440px}
.how h2{font-size:26px;font-weight:600;color:var(--maroon);margin-bottom:10px}
.how p{font-size:13px;line-height:1.7;color:var(--muted);margin-bottom:18px}
.btn{display:inline-block;background:var(--red);color:var(--white);font-size:11px;font-weight:700;letter-spacing:.6px;padding:10px 16px;text-transform:uppercase}
.video-thumb{position:absolute;left:820px;top:222px;width:292px;height:164px;background:linear-gradient(135deg,#4a3a30,#8a6a4a 50%,#3a3028)}
.video-thumb svg{position:absolute;left:122px;top:58px}

/* product band */
.product-band{position:absolute;top:992px;left:0;width:1200px;height:448px;background:var(--charcoal)}
.product-card{position:absolute;top:26px;width:304px;color:#bbb}
.product-card h3{color:var(--white);font-size:20px;font-weight:600;line-height:1.3;height:56px;margin-bottom:24px}
.product-photo{height:180px;margin-bottom:20px}
.product-card p{font-size:12px;line-height:1.6;margin-bottom:16px;height:78px}
.card-a{left:88px}.card-b{left:448px}.card-c{left:808px}

/* gallery */
.gallery{position:absolute;top:1440px;left:0;width:1200px;height:320px;background:var(--light)}
.gallery h2{position:absolute;left:88px;top:44px;font-size:26px;font-weight:600;color:var(--ink)}
.hex-row{position:absolute;left:88px;top:112px;width:1024px;display:flex;justify-content:space-between}
.hex{width:138px;height:160px;clip-path:polygon(50% 0,100% 25%,100% 75%,50% 100%,0 75%,0 25%)}
.hex:nth-child(even){margin-top:20px}

/* sale */
.sale{position:absolute;top:1770px;left:88px;width:1024px;height:290px;background:var(--white);box-shadow:0 1px 4px rgba(0,0,0,.1)}
.sale-copy{position:absolute;left:40px;top:34px;width:520px}
.sale-copy h2{font-size:28px;font-weight:600;color:var(--maroon);margin-bottom:12px}
.sale-copy .lead{font-size:14px;font-weight:700;color:var(--ink);margin-bottom:8px;line-height:1.5}
.sale-copy p{font-size:13px;line-height:1.7;color:var(--muted);margin-bottom:20px}
.sale-photo{position:absolute;left:612px;top:14px;width:398px;height:262px;background:linear-gradient(160deg,#b87a4a,#7a4a2a 45%,#c0a080 80%,#8a8a80)}

/* footer */
.site-footer{position:absolute;top:2080px;left:0;width:1200px;height:224px;background:var(--charcoal-dark);color:#aaa}
.footer-col{position:absolute;top:26px}
.footer-col h4{color:var(--white);font-size:12px;font-weight:700;letter-spacing:.6px;text-transform:uppercase;margin-bottom:14px}
.footer-col ul{font-size:12px;line-height:2}
.footer-col li::before{content:"› ";color:var(--red)}
.two-up{display:grid;grid-template-columns:90px 110px;column-gap:10px}
.col-nav{left:88px}.col-cat{left:348px}.col-connect{left:640px}.col-news{left:850px;width:262px}
.news-input{width:262px;height:34px;background:#333;border:1px solid #444;color:#888;font-size:12px;padding:8px 10px;margin-bottom:10px}
.col-news .btn{float:right}
.copyright{position:absolute;bottom:0;left:0;width:1200px;height:36px;background:#151515;font-size:11px;text-align:center;line-height:36px;color:#777}
</style>
</head>
<body>

<header class="site-nav">
  <ul class="nav-left"><li>HOME</li><li>ABOUT US</li><li>GALLERY</li><li>SHOP</li></ul>
  <a class="brand" href="#"><span class="brand-dot"></span><span class="brand-name">Halvor<br>Kettleworks</span></a>
  <ul class="nav-right"><li>BLOG</li><li>BOOKS</li><li>LINKS</li><li>CONTACT US</li></ul>
</header>

<section class="hero" role="img" aria-label="Photo of distillers tending a copper still outdoors">
  <h1 class="hero-caption">Distillation Equipment, Copper Still, Moonshine Still Sale, Ethanol, Vodka, Essential Oil...</h1>
  <div class="hero-dots"><span></span><span></span><span></span></div>
</section>

<section class="intro">
  <aside class="category-box">
    <h3>Select Category</h3>
    <ul>
      <li><svg width="6" height="8"><path d="M0 0l6 4-6 4z" fill="#9b2a31"/></svg>Stills</li>
      <li><svg width="6" height="8"><path d="M0 0l6 4-6 4z" fill="#9b2a31"/></svg>Essential Oils</li>
      <li><svg width="6" height="8"><path d="M0 0l6 4-6 4z" fill="#9b2a31"/></svg>Alcohol Fuel</li>
      <li><svg width="6" height="8"><path d="M0 0l6 4-6 4z" fill="#9b2a31"/></svg>Cannabis</li>
      <li><svg width="6" height="8"><path d="M0 0l6 4-6 4z" fill="#9b2a31"/></svg>Books</li>
      <li><svg width="6" height="8"><path d="M0 0l6 4-6 4z" fill="#9b2a31"/></svg>Home Distillers</li>
      <li><svg width="6" height="8"><path d="M0 0l6 4-6 4z" fill="#9b2a31"/></svg>Vodka Still</li>
      <li><svg width="6" height="8"><path d="M0 0l6 4-6 4z" fill="#9b2a31"/></svg>Heat Control</li>
      <li><svg width="6" height="8"><path d="M0 0l6 4-6 4z" fill="#9b2a31"/></svg>Distillery</li>
    </ul>
  </aside>

  <div class="intro-copy">
    <h2>Welcome to Our Website</h2>
    <p>Every still we build starts as a flat sheet of copper and ends as a working piece of equipment. We hammer, fold and solder each seam by hand so your first run is clean, safe and full of flavor. Browse the categories to find the right setup for your craft.</p>
  </div>

  <div class="how">
    <h2>How it Works</h2>
    <p>Pick a still size, choose your column and condenser, then place your order. We build it to your spec, pressure test every joint and ship it ready to run. Watch the short video to see a full build from sheet to finished still.</p>
    <a class="btn" href="#">Watch Video</a>
  </div>

  <div class="video-thumb" role="img" aria-label="Video still of a copper still being assembled">
    <svg width="48" height="48" viewBox="0 0 48 48"><circle cx="24" cy="24" r="22" fill="rgba(0,0,0,.45)" stroke="#fff" stroke-width="2"/><path d="M19 15l14 9-14 9z" fill="#fff"/></svg>
  </div>
</section>

<section class="product-band">
  <article class="product-card card-a">
    <h3>Home Distillers! We sell Copper Stills.</h3>
    <div class="product-photo" role="img" aria-label="Photo of a small copper pot still" style="background:linear-gradient(160deg,#8a8a8a,#c9a070 50%,#5a5a5a)"></div>
    <p>Small pot stills for the hobby distiller who wants real copper at home. Each one is hand folded and soldered, sized for a kitchen stove and easy to clean after every run.</p>
    <a class="btn" href="#">Read More</a>
  </article>
  <article class="product-card card-b">
    <h3>Micro Distillery Equipment- Copper Stills for Sale!</h3>
    <div class="product-photo" role="img" aria-label="Photo of a copper still column with fittings" style="background:linear-gradient(160deg,#6a6a6a,#b88a5a 50%,#4a4a4a)"></div>
    <p>Larger reflux and pot stills built for licensed craft producers. Thicker copper, bigger boilers and fittings that match standard brewery gear so you can scale up without starting over.</p>
    <a class="btn" href="#">Read More</a>
  </article>
  <article class="product-card card-c">
    <h3>Fenwick Herbal Extractor- Make Cannabis Oil with Alcohol!</h3>
    <div class="product-photo" role="img" aria-label="Photo of a herbal extractor among green plants" style="background:linear-gradient(160deg,#3a5a2a,#6a8a4a 50%,#2a3a1a)"></div>
    <p>A compact extractor that pulls oils and resins with food grade alcohol. Gentle heat, a sealed copper body and a simple recovery step let you reuse your solvent run after run.</p>
    <a class="btn" href="#">Read More</a>
  </article>
</section>

<section class="gallery">
  <h2>Photo Gallery</h2>
  <div class="hex-row">
    <div class="hex" role="img" aria-label="Gallery photo of a copper still outdoors" style="background:linear-gradient(150deg,#6a7a4a,#b08050)"></div>
    <div class="hex" role="img" aria-label="Gallery photo of a copper still in a workshop" style="background:linear-gradient(150deg,#8a6a4a,#c09060)"></div>
    <div class="hex" role="img" aria-label="Gallery photo of copper still parts" style="background:linear-gradient(150deg,#a07a50,#5a4a3a)"></div>
    <div class="hex" role="img" aria-label="Gallery photo of a steel and copper boiler" style="background:linear-gradient(150deg,#9a9a9a,#b88a5a)"></div>
    <div class="hex" role="img" aria-label="Gallery photo of a still column" style="background:linear-gradient(150deg,#7a7a7a,#c09a6a)"></div>
    <div class="hex" role="img" aria-label="Gallery photo of a copper pot still" style="background:linear-gradient(150deg,#b07a4a,#6a5040)"></div>
    <div class="hex" role="img" aria-label="Gallery photo of a distiller in a field" style="background:linear-gradient(150deg,#5a7a3a,#9aa070)"></div>
  </div>
</section>

<section class="sale">
  <div class="sale-copy">
    <h2>Copper Still for Sale!</h2>
    <p class="lead">Buy a Still today! Made by hand in the<br>Pacific Northwest.</p>
    <p>Every still leaves our shop tested and ready to use. Pick your size, add a thumper or column, and we will ship it straight to your door.</p>
    <a class="btn" href="#">Buy a Still Here</a>
  </div>
  <div class="sale-photo" role="img" aria-label="Photo of a finished copper still on a workbench"></div>
</section>

<footer class="site-footer">
  <div class="footer-col col-nav">
    <h4>Navigation</h4>
    <ul class="two-up"><li>Home</li><li>Shop</li><li>About Us</li><li>Blog</li><li>Contact Us</li><li>Books</li><li>Gallery</li><li>Links</li></ul>
  </div>
  <div class="footer-col col-cat">
    <h4>Categories</h4>
    <ul class="two-up"><li>Stills</li><li>Books</li><li>Essential Oils</li><li>Home Distillers</li><li>Alcohol Fuel</li><li>Vodka Still</li><li>Cannabis</li><li>Heat Control</li></ul>
  </div>
  <div class="footer-col col-connect">
    <h4>Connect Us</h4>
    <ul><li>Friendwall</li><li>Chirpline</li><li>Snapvale</li></ul>
  </div>
  <div class="footer-col col-news">
    <h4>Newsletter Sign Up</h4>
    <div class="news-input">Enter email address</div>
    <a class="btn" href="#">Read More</a>
  </div>
  <div class="copyright">Copyright © 2016 Halvor Kettleworks. All Rights Reserved.</div>
</footer>

</body>
</html>
```